Option Sheet

We need a one page option sheet with a left to right reading of the five options. It should be a one sheet, multiple colors and definitive separations between options This is used in a sales consultation. Backround or colors not in option need to have the follow RGB value (5 red, 20 green, 63 blue)

We added a smaller text file, please change that point

Target Market(s)

Divorce

Industry/Entity Type

Legal

Requirements
Must have
• 1) All five options left to right
• 2)language included in sheet

```html
<!DOCTYPE html>
<html lang="en">
<head>
<meta charset="UTF-8">
<title>Five Options – Divorce</title>
<link href="https://fonts.googleapis.com/css2?family=Cinzel:wght@700;900&family=Nunito+Sans:wght@400;600;700&display=swap" rel="stylesheet">
<style>
  :root{
    --page:#05143f;
    --ink:#0b1d52;
    --white:#ffffff;
    --red-deep:#ff0000;  --red-mid:#ff2a2a;  --red-light:#fbb4b4;
    --clay-deep:#cf7150; --clay-mid:#d88a6c; --clay-light:#efd3cb;
    --sun-deep:#fcee76;  --sun-mid:#fbf08a;  --sun-light:#f4f0dc;
    --leaf-deep:#009341; --leaf-mid:#22a35a; --leaf-light:#bfe2cd;
    --sky-deep:#009fe0;  --sky-mid:#1aa7e2;  --sky-light:#b4e1f5;
  }
  *{box-sizing:border-box;margin:0;padding:0}
  html,body{width:848px;height:1200px;overflow:hidden;background:var(--page)}
  .sheet{position:relative;width:848px;height:1200px;background:var(--page);font-family:"Nunito Sans",sans-serif}
  .sheet__title{position:absolute;left:0;right:0;top:16px;text-align:center;color:var(--white);font-family:"Cinzel",serif;font-weight:700;line-height:1}
  .sheet__title-top{display:block;font-size:46px;letter-spacing:7px}
  .sheet__title-main{display:block;font-size:52px;letter-spacing:2px;margin-top:6px}

  .option{position:absolute;left:20px;width:799px;height:172px}
  .option--nothing{top:163px;--deep:var(--red-deep);--mid:var(--red-mid);--light:var(--red-light)}
  .option--counseling{top:376px;--deep:var(--clay-deep);--mid:var(--clay-mid);--light:var(--clay-light)}
  .option--diy{top:588px;--deep:var(--sun-deep);--mid:var(--sun-mid);--light:var(--sun-light)}
  .option--limited{top:800px;--deep:var(--leaf-deep);--mid:var(--leaf-mid);--light:var(--leaf-light)}
  .option--hire{top:1014px;--deep:var(--sky-deep);--mid:var(--sky-mid);--light:var(--sky-light)}

  .option__band{position:absolute;inset:0;background:linear-gradient(90deg,var(--light) 10%,var(--mid) 75%,var(--deep))}
  .option__num-panel{position:absolute;inset:0;background:var(--deep);clip-path:polygon(0 0,147px 0,83px 100%,0 100%)}
  .option__num-edge{position:absolute;inset:0;background:var(--deep);opacity:.85;clip-path:polygon(147px 0,160px 0,96px 100%,83px 100%)}
  .option__num{position:absolute;left:22px;top:55px;color:var(--white);font-family:"Cinzel",serif;font-weight:900;font-size:50px;line-height:1;text-shadow:2px 3px 4px rgba(0,0,0,.55)}

  .option__fold{position:absolute;left:239px;top:-22px;width:12px;height:22px}
  .option__title-tab{position:absolute;left:250px;top:-22px;width:339px;height:50px;background:var(--deep);box-shadow:2px 3px 5px rgba(0,0,0,.3);display:flex;align-items:center;justify-content:center}
  .option__title{font-family:"Cinzel",serif;font-weight:700;font-size:25px;letter-spacing:1px;color:var(--ink);text-shadow:1px 2px 3px rgba(0,0,0,.35);white-space:nowrap}
  .option--limited .option__title{font-size:21px}

  .option__side-tab{position:absolute;left:747px;top:17px;width:64px;height:80px;background:var(--deep);clip-path:polygon(0 0,100% 0,100% 100%,44% 100%)}
  .option__check{position:absolute;left:781px;top:45px;width:22px;height:20px;border:2px solid var(--white);border-radius:3px}

  .option__label{position:absolute;width:270px;text-align:right;right:auto;left:0;font-weight:700;font-size:19px;color:var(--ink);text-shadow:1px 2px 3px rgba(0,0,0,.3);white-space:nowrap}
  .option__label--pro{top:45px}
  .option__label--con{top:101px}

  .option__list{position:absolute;left:281px;list-style:none;color:var(--ink)}
  .option__list li{position:relative;padding-left:12px;white-space:nowrap}
  .option__list li::before{content:"•";position:absolute;left:0}
  .option__list--pro{top:40px;font-size:17.5px;line-height:17px;letter-spacing:.3px;font-weight:600}
  .option__list--con{top:91px;font-size:16.5px;line-height:17px;font-weight:600}
  .option__list--small{font-size:14.5px;letter-spacing:-.2px;font-weight:400;color:#0a1a4a}
  .option__list .wrap{white-space:normal;width:505px}
</style>
</head>
<body>
<main class="sheet">
  <h1 class="sheet__title">
    <span class="sheet__title-top">FIVE OPTIONS</span>
    <span class="sheet__title-main">DIVORCE</span>
  </h1>

  <section class="option option--nothing">
    <div class="option__band"></div>
    <div class="option__num-panel"></div>
    <div class="option__num-edge"></div>
    <span class="option__num">01</span>
    <svg class="option__fold" viewBox="0 0 12 22"><polygon points="0,22 12,0 12,22" fill="#b00000"/></svg>
    <div class="option__title-tab"><h2 class="option__title">DO NOTHING</h2></div>
    <div class="option__side-tab"></div><span class="option__check"></span>
    <span class="option__label option__label--pro">Advantages:</span>
    <ul class="option__list option__list--pro"><li>Stay married</li><li>No life Changes</li></ul>
    <span class="option__label option__label--con">Disadvantages:</span>
    <ul class="option__list option__list--con"><li>Remain unhappy, depressed, anxious</li><li>Money and assets may disappear</li><li>What is going to change?</li></ul>
  </section>

  <section class="option option--counseling">
    <div class="option__band"></div>
    <div class="option__num-panel"></div>
    <div class="option__num-edge"></div>
    <span class="option__num">02</span>
    <svg class="option__fold" viewBox="0 0 12 22"><polygon points="0,22 12,0 12,22" fill="#a4553a"/></svg>
    <div class="option__title-tab"><h2 class="option__title">GO TO COUNSELING</h2></div>
    <div class="option__side-tab"></div><span class="option__check"></span>
    <span class="option__label option__label--pro">Advantages:</span>
    <ul class="option__list option__list--pro"><li>Reconcile marriage</li><li>Help make a better life</li></ul>
    <span class="option__label option__label--con">Disadvantages:</span>
    <ul class="option__list option__list--con option__list--small"><li>Past issues are highlighted and may drudge up old wounds</li><li>It may just clarify the reasons you need to separate and/or divorce</li><li>Both parties must be invested and willing to participate</li></ul>
  </section>

  <section class="option option--diy">
    <div class="option__band"></div>
    <div class="option__num-panel"></div>
    <div class="option__num-edge"></div>
    <span class="option__num">03</span>
    <svg class="option__fold" viewBox="0 0 12 22"><polygon points="0,22 12,0 12,22" fill="#d8c84e"/></svg>
    <div class="option__title-tab"><h2 class="option__title">DO IT YOURSELF</h2></div>
    <div class="option__side-tab"></div><span class="option__check"></span>
    <span class="option__label option__label--pro">Advantages:</span>
    <ul class="option__list option__list--pro"><li>No attorney fees</li><li>You are your on attorney</li></ul>
    <span class="option__label option__label--con">Disadvantages:</span>
    <ul class="option__list option__list--con option__list--small" style="top:84px"><li>People often find that what is “fair,” may in fact, not be truly fair</li><li>Often times, people do not know the risks</li><li>Complicated legal system within intrigue rules</li><li>Unsure how to complete the necessary paperwork and meet the deadlines</li></ul>
  </section>

  <section class="option option--limited">
    <div class="option__band"></div>
    <div class="option__num-panel"></div>
    <div class="option__num-edge"></div>
    <span class="option__num">04</span>
    <svg class="option__fold" viewBox="0 0 12 22"><polygon points="0,22 12,0 12,22" fill="#006a2e"/></svg>
    <div class="option__title-tab"><h2 class="option__title">LIMITED REPRESENTATION</h2></div>
    <div class="option__side-tab"></div><span class="option__check"></span>
    <span class="option__label option__label--pro">Advantages:</span>
    <ul class="option__list option__list--pro"><li class="wrap">Balance between going alone and our limited involvement in the case</li></ul>
    <span class="option__label option__label--con">Disadvantages:</span>
    <ul class="option__list option__list--con option__list--small" style="top:86px;left:278px"><li>Our terms may not benefit from our legal knowledge</li><li>The legal consequences of your legal documents will not be explained<br>to you so that you can formulate a plan for handling the rest of your case.</li><li>Your spouse or other parties may cause your legal fees to increase<br>significantly without action on your part</li></ul>
  </section>

  <section class="option option--hire">
    <div class="option__band"></div>
    <div class="option__num-panel"></div>
    <div class="option__num-edge"></div>
    <span class="option__num">05</span>
    <svg class="option__fold" viewBox="0 0 12 22"><polygon points="0,22 12,0 12,22" fill="#0072a6"/></svg>
    <div class="option__title-tab"><h2 class="option__title">HIRE US</h2></div>
    <div class="option__side-tab"></div><span class="option__check"></span>
    <span class="option__label option__label--pro" style="top:46px">Advantages:</span>
    <ul class="option__list option__list--pro" style="top:44px;line-height:14.5px;font-size:16px"><li>Gain the full benefits of our experience</li><li>Have a team of Family Law focus attorneys</li><li>Often saves you or makes you money in the long run</li><li>Save you time, energy and stress</li></ul>
    <span class="option__label option__label--con" style="top:116px">Disadvantages:</span>
    <ul class="option__list option__list--con" style="top:118px;font-size:17.5px"><li>Initial cost</li></ul>
  </section>
</main>
</body>
</html>
```